Need new website for my business

I want to design a new Irrigation website for our business. What we are looking for is to have a residential section that describes providing for irrigation service for residential customers in homeowners Association. From startups to service to winterization in full residential installs.
A commercial section on our webpage describing. installation of commercial Irrigation systems. Service start-up of systems. To winterizations. Offering contract service plans for commercial customers.
Service for both commercial residential include making sure all zones are operating check for leaks adjust spray nozzles in rotors making sure all irrigation heads rotate, and are not stuck or damaged making sure that we have full coverage of each Irrigation zone for lawns. In all drip irrigation is Functioning in watering the plants accordingly. Adjusting control settings to make sure you have the right watering times during the hot dry months.
Have a landscape lighting tab:
Describing what landscape lighting and what it does to enhance curb, appeal, highlight architectural, features of landscape and transferring your outdoor space into inviting visual stunning areas with low-voltage landscape lighting
And a residential snow plowing for the Falmouth Maine area. In commercial snow, plowing and snow removal covering Scarborough south portland Portland Falmouth in Cumberland Maine for commercial Snow services. From plow & Salting parking lots to Snow removing, and Snow displacement.
we started a website but it needs a up lift and bring it to pop
our web site is willowbrookyards314.com
here are a few websites that we really like:
www.sprinklecoastal.com
www.dewpointwatering.com
www.verdantlawnsystems.com
Industry/Entity Type
Irrigation & Landscape Lighting
Coding
Coded - Design and coding required
Number of Pages Required
4 page

```html
<!DOCTYPE html>
<html lang="en">
<head>
<meta charset="utf-8">
<title>Willowbrook Yards — Irrigation, Landscape Lighting &amp; Snow Services</title>
<link href="https://fonts.googleapis.com/css2?family=Inter:wght@400;500;600&family=Newsreader:ital,opsz,wght@0,6..72,500;0,6..72,600;1,6..72,500&display=swap" rel="stylesheet">
<style>
:root{
  --ink:#0f172a;
  --body:#475569;
  --muted:#64748b;
  --line:#e2e8f0;
  --brand:#0ea5e9;
  --brand-dark:#0284c7;
  --green:#22a04b;
  --soft:#f1f6fb;
  --navy:#0f1a33;
  --white:#ffffff;
}
*{box-sizing:border-box;margin:0;padding:0}
html,body{width:1200px;height:2891px;overflow:hidden}
body{font-family:"Inter",sans-serif;color:var(--ink);background:var(--white);position:relative}
.serif{font-family:"Newsreader",serif}
.abs{position:absolute}
a{text-decoration:none;color:inherit}

/* Header */
.site-header{position:absolute;top:0;left:0;width:1200px;height:67px;background:var(--white);border-bottom:1px solid #eef2f6;z-index:2}
.brand{position:absolute;left:90px;top:20px;display:flex;align-items:center;gap:8px;font-size:21px;font-weight:600;color:var(--green)}
.brand .dot{width:14px;height:14px;border-radius:50%;background:var(--green)}
.nav{position:absolute;right:91px;top:18px;display:flex;align-items:center;gap:27px;font-size:13px;color:#334155}
.nav .cta{background:var(--brand);color:var(--white);font-weight:500;padding:8px 17px;border-radius:16px}

/* Hero */
.hero{position:absolute;top:67px;left:0;width:1200px;height:562px;background:linear-gradient(180deg,#eaf5fd 0%,#f5fafe 70%,#ffffff 100%)}
.pill{display:inline-flex;align-items:center;gap:7px;background:var(--white);border:1px solid #e6eef0;border-radius:12px;padding:4px 10px;font-size:10.5px;font-weight:500;letter-spacing:.3px;color:#166534}
.pill .d{width:6px;height:6px;border-radius:50%;background:#4ade80}
.hero .pill{position:absolute;left:90px;top:67px}
.hero h1{position:absolute;left:90px;top:111px;font-family:"Newsreader",serif;font-weight:600;font-size:56px;line-height:61px;letter-spacing:-.5px;color:var(--ink)}
.hero h1 em{font-style:italic;font-weight:500;color:var(--brand)}
.hero p{position:absolute;left:90px;top:310px;width:560px;font-size:17px;line-height:27px;color:var(--body)}
.btn{position:absolute;height:45px;border-radius:6px;font-size:14px;font-weight:500;display:flex;align-items:center;justify-content:center;gap:8px}
.btn-primary{left:90px;top:398px;width:186px;background:var(--brand);color:var(--white);box-shadow:0 6px 14px rgba(14,165,233,.3)}
.btn-ghost{left:290px;top:398px;width:171px;background:var(--white);border:1px solid var(--line);color:#1e293b}

/* Irrigation */
.irrigation{position:absolute;top:629px;left:0;width:1200px;height:651px}
.section-title{font-family:"Newsreader",serif;font-weight:500;font-size:29px;color:var(--ink)}
.irrigation .section-title{position:absolute;left:90px;top:70px}
.lead{font-size:15.5px;line-height:24.5px;color:var(--body)}
.irrigation .lead{position:absolute;left:90px;top:123px;width:490px}
.svc-card{position:absolute;left:90px;width:483px;height:163px;border-radius:12px;padding:24px 24px 0 74px}
.svc-card.res{top:224px;background:#f6fbfd}
.svc-card.com{top:407px;background:#fcfdf7;border:1.5px solid #ecefdf}
.svc-icon{position:absolute;left:22px;top:24px;width:36px;height:36px;border-radius:9px;display:flex;align-items:center;justify-content:center}
.svc-card.res .svc-icon{background:#eaf6fd}
.svc-card.com .svc-icon{background:#e7f5ea}
.svc-card h3{font-family:"Newsreader",serif;font-weight:600;font-size:16px;color:var(--ink);margin-top:-2px}
.svc-card p{font-size:12px;line-height:19px;color:var(--body);margin-top:8px;width:390px}
.ticks{list-style:none;margin-top:10px}
.ticks li{display:flex;align-items:center;gap:8px;font-size:12px;color:#334155;height:23px}

.maint-card{position:absolute;left:626px;top:69px;width:483px;height:309px;border-radius:16px;background:linear-gradient(135deg,#1b3354 0%,#142846 45%,#101d38 100%);box-shadow:0 20px 40px rgba(15,23,42,.25);padding:34px 33px;color:var(--white)}
.maint-card h3{font-family:"Newsreader",serif;font-weight:500;font-size:21px}
.maint-card .intro{font-size:11.5px;line-height:17px;color:#9fb0c8;margin-top:8px;width:420px}
.checks{position:absolute;left:33px;top:130px;width:418px;display:grid;grid-template-columns:218px 200px;row-gap:20px}
.check{display:flex;gap:10px}
.check svg{flex:none;margin-top:1px}
.check b{display:block;font-family:"Newsreader",serif;font-weight:600;font-size:11.5px;color:#e5ecf5}
.check span{display:block;font-size:10.5px;color:#6f819c;margin-top:3px}
.maint-card .rule{position:absolute;left:33px;top:235px;width:418px;height:1px;background:rgba(255,255,255,.1)}
.maint-card .timer{position:absolute;left:33px;top:251px}

/* Lighting */
.lighting{position:absolute;top:1280px;left:0;width:1200px;height:698px;background:var(--soft)}
.tag{display:inline-block;background:var(--white);border-radius:10px;padding:4px 10px;font-size:10px;font-weight:500;letter-spacing:.4px;color:var(--brand)}
.lighting .tag{position:absolute;left:90px;top:121px}
.lighting .section-title{position:absolute;left:90px;top:157px}
.lighting .lead{position:absolute;left:90px;top:207px;width:500px;font-size:15.5px;line-height:24px}
.text-link{position:absolute;left:90px;top:296px;font-size:12.5px;font-weight:500;color:var(--brand);display:flex;align-items:center;gap:6px}
.photo{position:absolute;left:621px;top:84px;width:487px;height:271px;border-radius:12px;border:3px solid var(--white);box-shadow:0 14px 30px rgba(15,23,42,.15);background:linear-gradient(120deg,#2b2a24 0%,#6b4a24 28%,#c98a3d 42%,#3b4650 60%,#c7894a 78%,#2f3c3c 100%)}
.float-badge{position:absolute;left:600px;top:315px;width:168px;height:61px;border-radius:8px;background:var(--white);box-shadow:0 10px 24px rgba(15,23,42,.14);display:flex;align-items:center;gap:10px;padding:0 14px}
.float-badge .bulb{width:34px;height:34px;border-radius:50%;background:#fdf3c7;display:flex;align-items:center;justify-content:center}
.float-badge small{display:block;font-size:9.5px;letter-spacing:.3px;color:var(--muted)}
.float-badge strong{display:block;font-size:12px;font-weight:600;color:var(--ink);margin-top:2px}
.feature{position:absolute;top:412px;width:321px;height:204px;background:var(--white);border-radius:12px;padding:26px 27px}
.feature .ficon{width:40px;height:40px;border-radius:50%;display:flex;align-items:center;justify-content:center}
.feature h3{font-family:"Newsreader",serif;font-weight:600;font-size:16.5px;margin-top:14px}
.feature p{font-size:12px;line-height:19px;color:var(--body);margin-top:10px}

/* Winter */
.winter{position:absolute;top:1978px;left:0;width:1200px;height:570px}
.eyebrow{position:absolute;left:90px;top:80px;display:flex;align-items:center;gap:10px;font-size:10.5px;font-weight:500;letter-spacing:1px;color:#94a3b8}
.eyebrow i{display:block;width:26px;height:1px;background:#cbd5e1}
.winter .section-title{position:absolute;left:90px;top:106px}
.winter .lead{position:absolute;left:90px;top:161px;width:480px;font-size:15.5px;line-height:24px}
.snow-card{position:absolute;left:90px;width:489px;height:120px;border-radius:10px;padding:22px 21px}
.snow-card.res{top:236px;background:#f8fbfd}
.snow-card.com{top:369px;background:var(--white);border:1.5px solid var(--line)}
.snow-card h3{font-family:"Newsreader",serif;font-weight:600;font-size:14.5px}
.snow-card p{font-size:12px;color:var(--body);margin-top:8px}
.snow-card .ico{position:absolute;right:20px;top:22px}
.chips{display:flex;gap:8px;margin-top:12px}
.chips span{font-size:10px;color:#334155;border:1px solid var(--line);border-radius:4px;padding:3px 7px;background:var(--white)}

/* Footer */
.site-footer{position:absolute;top:2548px;left:0;width:1200px;height:343px;background:var(--navy);color:#cbd5e1}
.site-footer .brand{left:90px;top:62px;color:var(--white)}
.site-footer .brand .dot{background:var(--white)}
.foot-about{position:absolute;left:90px;top:116px;width:265px;font-size:12px;line-height:19px;color:#94a3b8}
.foot-site{position:absolute;left:90px;top:193px;font-size:12px;color:var(--brand)}
.foot-col{position:absolute;top:60px}
.foot-col h4{font-family:"Newsreader",serif;font-weight:600;font-size:12px;color:var(--white);margin-bottom:12px}
.foot-col li{list-style:none;font-size:12px;color:#94a3b8;height:27px}
.foot-col.contact li{display:flex;gap:10px}
.foot-rule{position:absolute;left:90px;top:249px;width:1019px;height:1px;background:#232e48}
.legal{position:absolute;left:90px;top:277px;font-size:10.5px;color:#94a3b8}
.legal-links{position:absolute;right:91px;top:277px;font-size:10.5px;color:#94a3b8;display:flex;gap:14px}
</style>
</head>
<body>

<header class="site-header">
  <a class="brand" href="#"><span class="dot"></span>Willowbrook Yards</a>
  <nav class="nav">
    <a href="#irrigation">Irrigation</a>
    <a href="#lighting">Lighting</a>
    <a href="#snow">Snow Services</a>
    <a class="cta" href="#quote">Get a Quote</a>
  </nav>
</header>

<section class="hero">
  <span class="pill"><span class="d"></span>SERVING GREATER PORTLAND &amp; FALMOUTH</span>
  <h1>Professional Irrigation &amp;<br><em>Landscape Lighting</em><br>Solutions.</h1>
  <p>Transforming outdoor spaces with expert irrigation systems, stunning low-voltage lighting, and reliable snow removal services.</p>
  <a class="btn btn-primary" href="#quote">Schedule Service
    <svg width="12" height="12" viewBox="0 0 24 24" fill="none" stroke="currentColor" stroke-width="2.5" stroke-linecap="round" stroke-linejoin="round"><path d="M5 12h14M13 6l6 6-6 6"/></svg></a>
  <a class="btn btn-ghost" href="#portfolio">View Our Portfolio</a>
</section>

<section class="irrigation" id="irrigation">
  <h2 class="section-title">Irrigation Systems</h2>
  <p class="lead">We ensure lush landscapes through precision water management. Whether it's a new installation or seasonal maintenance, our team handles every drop using smart, water-efficient technology.</p>

  <article class="svc-card res">
    <div class="svc-icon"><svg width="18" height="18" viewBox="0 0 24 24" fill="none" stroke="#0ea5e9" stroke-width="2" stroke-linecap="round" stroke-linejoin="round"><path d="M3 10l9-7 9 7v10a1 1 0 0 1-1 1h-5v-6H9v6H4a1 1 0 0 1-1-1z"/></svg></div>
    <h3>Residential Services</h3>
    <p>Specialized care for homeowners and HOAs. We manage the full lifecycle of your lawn's hydration.</p>
    <ul class="ticks">
      <li><svg width="12" height="12" viewBox="0 0 24 24" fill="none" stroke="#22a04b" stroke-width="2.5" stroke-linecap="round"><path d="M4 12l5 5L20 6"/></svg>System Start-ups &amp; Winterization</li>
      <li><svg width="12" height="12" viewBox="0 0 24 24" fill="none" stroke="#22a04b" stroke-width="2.5" stroke-linecap="round"><path d="M4 12l5 5L20 6"/></svg>Full Residential Installs</li>
    </ul>
  </article>

  <article class="svc-card com">
    <div class="svc-icon"><svg width="18" height="18" viewBox="0 0 24 24" fill="none" stroke="#22a04b" stroke-width="2" stroke-linecap="round" stroke-linejoin="round"><rect x="4" y="3" width="16" height="18" rx="1"/><path d="M9 21v-4h6v4M8 7h2M14 7h2M8 11h2M14 11h2"/></svg></div>
    <h3>Commercial Solutions</h3>
    <p>Robust irrigation strategies for businesses. We offer contract service plans to keep your property professional year-round.</p>
    <ul class="ticks">
      <li><svg width="12" height="12" viewBox="0 0 24 24" fill="none" stroke="#22a04b" stroke-width="2.5" stroke-linecap="round"><path d="M4 12l5 5L20 6"/></svg>Commercial Installation</li>
      <li><svg width="12" height="12" viewBox="0 0 24 24" fill="none" stroke="#22a04b" stroke-width="2.5" stroke-linecap="round"><path d="M4 12l5 5L20 6"/></svg>Service Contracts</li>
    </ul>
  </article>

  <aside class="maint-card">
    <h3>Comprehensive Maintenance</h3>
    <p class="intro">Our rigorous 12-point inspection ensures efficiency and coverage for both commercial and residential zones.</p>
    <div class="checks">
      <div class="check"><svg width="16" height="16" viewBox="0 0 24 24" fill="none" stroke="#38bdf8" stroke-width="2" stroke-linecap="round"><path d="M7 17a4 4 0 0 1-1-7l3-6 3 6a4 4 0 0 1-5 7zM15 19a3 3 0 0 0 3-5l-2-4-2 4a3 3 0 0 0 1 5z"/></svg><div><b>Zone Operations</b><span>Full coverage verification.</span></div></div>
      <div class="check"><svg width="16" height="16" viewBox="0 0 24 24" fill="none" stroke="#38bdf8" stroke-width="2" stroke-linecap="round"><circle cx="11" cy="11" r="7"/><path d="M20 20l-4-4"/></svg><div><b>Leak Detection</b><span>Line &amp; head checks.</span></div></div>
      <div class="check"><svg width="16" height="16" viewBox="0 0 24 24" fill="none" stroke="#38bdf8" stroke-width="2" stroke-linecap="round"><path d="M4 7h10M18 7h2M4 17h4M12 17h8"/><circle cx="16" cy="7" r="2"/><circle cx="10" cy="17" r="2"/></svg><div><b>Nozzle Adjustment</b><span>Precision tuning.</span></div></div>
      <div class="check"><svg width="16" height="16" viewBox="0 0 24 24" fill="none" stroke="#38bdf8" stroke-width="2" stroke-linecap="round"><circle cx="12" cy="6" r="3"/><circle cx="12" cy="14" r="3"/><path d="M12 17v5"/></svg><div><b>Drip Irrigation</b><span>Bed &amp; plant checks.</span></div></div>
    </div>
    <div class="rule"></div>
    <div class="check timer"><svg width="16" height="16" viewBox="0 0 24 24" fill="none" stroke="#38bdf8" stroke-width="2" stroke-linecap="round"><circle cx="12" cy="12" r="9"/><path d="M12 7v5l3 2"/></svg><div><b>Smart Timer Programming</b><span>Adjusting for local weather patterns to optimize usage.</span></div></div>
  </aside>
</section>

<section class="lighting" id="lighting">
  <span class="tag">ENHANCE CURB APPEAL</span>
  <h2 class="section-title">Landscape Lighting</h2>
  <p class="lead">Transform your outdoor space into an inviting, visually stunning area with premium low-voltage landscape lighting. We design systems that highlight architectural features while improving safety.</p>
  <a class="text-link" href="#quote">Request a Design Consultation
    <svg width="11" height="11" viewBox="0 0 24 24" fill="none" stroke="currentColor" stroke-width="2.5" stroke-linecap="round" stroke-linejoin="round"><path d="M5 12h14M13 6l6 6-6 6"/></svg></a>

  <div class="photo" role="img" aria-label="Modern home at dusk with warm uplighting on the facade, trees and garden beds"></div>
  <div class="float-badge">
    <div class="bulb"><svg width="16" height="16" viewBox="0 0 24 24" fill="none" stroke="#eab308" stroke-width="2" stroke-linecap="round"><path d="M9 18h6M10 21h4M12 3a6 6 0 0 0-4 10.5c.7.7 1 1.5 1 2.5h6c0-1 .3-1.8 1-2.5A6 6 0 0 0 12 3z"/></svg></div>
    <div><small>ENERGY EFFICIENT</small><strong>Low-Voltage LED</strong></div>
  </div>

  <article class="feature" style="left:90px">
    <div class="ficon" style="background:#fff4e6"><svg width="18" height="18" viewBox="0 0 24 24" fill="none" stroke="#ea7a12" stroke-width="2" stroke-linecap="round" stroke-linejoin="round"><path d="M10 4l1.5 4.5L16 10l-4.5 1.5L10 16l-1.5-4.5L4 10l4.5-1.5zM18 3v4M16 5h4M17 16v4M15 18h4"/></svg></div>
    <h3>Architectural Highlights</h3>
    <p>Accentuate the unique features of your home's architecture and landscape design, creating depth and character after dark.</p>
  </article>
  <article class="feature" style="left:439px">
    <div class="ficon" style="background:#eaf6fd"><svg width="18" height="18" viewBox="0 0 24 24" fill="none" stroke="#0ea5e9" stroke-width="2" stroke-linecap="round"><path d="M2 12s4-7 10-7 10 7 10 7-4 7-10 7S2 12 2 12z"/><circle cx="12" cy="12" r="3"/></svg></div>
    <h3>Visual Appeal</h3>
    <p>Create an inviting atmosphere for evening entertainment or relaxation. Our low-voltage systems provide stunning visual impact.</p>
  </article>
  <article class="feature" style="left:788px">
    <div class="ficon" style="background:#eef2f6"><svg width="18" height="18" viewBox="0 0 24 24" fill="none" stroke="#475569" stroke-width="2" stroke-linecap="round" stroke-linejoin="round"><path d="M12 3l8 3v6c0 5-3.5 8-8 9-4.5-1-8-4-8-9V6z"/><path d="M9 12l2 2 4-4"/></svg></div>
    <h3>Safety &amp; Security</h3>
    <p>Illuminated pathways and perimeters not only look beautiful but deter intruders and ensure safe navigation at night.</p>
  </article>
</section>

<section class="winter" id="snow">
  <div class="eyebrow"><i></i>SEASONAL SERVICES</div>
  <h2 class="section-title">Winter Services</h2>
  <p class="lead">When winter hits Maine, we are ready. From plowing and salting parking lots to detailed snow removal and displacement.</p>

  <article class="snow-card res">
    <h3>Residential Plowing</h3>
    <p>Dedicated driveway clearing service.</p>
    <div class="chips"><span>Falmouth, ME</span></div>
    <svg class="ico" width="15" height="15" viewBox="0 0 24 24" fill="none" stroke="#38bdf8" stroke-width="2" stroke-linecap="round"><path d="M12 2v20M3 7l18 10M21 7L3 17M9 4l3 3 3-3M9 20l3-3 3 3"/></svg>
  </article>
  <article class="snow-card com">
    <h3>Commercial Snow Management</h3>
    <p>Plowing, salting, removal &amp; displacement for businesses.</p>
    <div class="chips"><span>Scarborough</span><span>South Portland</span><span>Portland</span></div>
    <svg class="ico" width="16" height="16" viewBox="0 0 24 24" fill="none" stroke="#94a3b8" stroke-width="2" stroke-linecap="round" stroke-linejoin="round"><path d="M2 6h12v10H2zM14 10h4l3 3v3h-7z"/><circle cx="6" cy="18" r="2"/><circle cx="17" cy="18" r="2"/></svg>
  </article>
</section>

<footer class="site-footer">
  <a class="brand" href="#"><span class="dot"></span>Willowbrook Yards</a>
  <p class="foot-about">Professional Landscape, Lighting &amp; Irrigation services for Southern Maine. Bringing your property to life.</p>
  <a class="foot-site" href="#">willowbrookyards314.com</a>

  <div class="foot-col" style="left:620px">
    <h4>Services</h4>
    <ul>
      <li>Residential Irrigation</li>
      <li>Commercial Irrigation</li>
      <li>Landscape Lighting</li>
      <li>Snow Plowing</li>
    </ul>
  </div>
  <div class="foot-col contact" style="left:885px">
    <h4>Contact</h4>
    <ul>
      <li style="height:43px;line-height:17px"><svg width="12" height="12" viewBox="0 0 24 24" fill="none" stroke="#0ea5e9" stroke-width="2"><path d="M12 22s7-7 7-12a7 7 0 0 0-14 0c0 5 7 12 7 12z"/><circle cx="12" cy="10" r="2"/></svg><span>Serving Falmouth, Portland,<br>Scarborough, and Cumberland, ME</span></li>
      <li><svg width="13" height="13" viewBox="0 0 24 24" fill="none" stroke="#0ea5e9" stroke-width="2" stroke-linecap="round"><path d="M5 3h4l2 5-3 2a11 11 0 0 0 6 6l2-3 5 2v4a2 2 0 0 1-2 2A17 17 0 0 1 3 5a2 2 0 0 1 2-2z"/></svg>(207) 555-0198</li>
      <li><svg width="13" height="13" viewBox="0 0 24 24" fill="none" stroke="#0ea5e9" stroke-width="2"><rect x="3" y="5" width="18" height="14" rx="2"/><path d="M3 7l9 6 9-6"/></svg>info@willowbrookyards314.com</li>
    </ul>
  </div>

  <div class="foot-rule"></div>
  <p class="legal">© 2024 Willowbrook Yards. All rights reserved.</p>
  <div class="legal-links"><a href="#">Privacy Policy</a><a href="#">Terms of Service</a></div>
</footer>

</body>
</html>
```